Corporate Branding - Web and Print

A UK based company will like to use an existing logo to create branding materials for all marketing related documents, including business card, prints, letterhead, Website, Twitter, Facebook, Instagram logo etc. This company serves high-end clientele in the fashion, health and wellness and as such high quality and class is of utmost importance.
Where the logo can be modernised without losing its character then experiment. The main thing is to have a corporate branding which can be used later for brochures, Business Plan infographics.
The prominent colour within the organisation is burnt orange with no secondary colour. However if you believe a secondary colour is needed then use it, otherwise keep it simple and classy. Any chosen colours have to match perfectly.
Target Market(s)
High net worth individuals
Industry/Entity Type
Health And Wellness
Contact Information for Business Card
classy
Look and feel
Each slider illustrates characteristics of the customer's brand and the style your logo design should communicate.

```html
<!DOCTYPE html>
<html lang="en">
<head>
<meta charset="utf-8">
<title>Velqara Business Card</title>
<link rel="stylesheet" href="https://fonts.googleapis.com/css2?family=Montserrat:wght@500;600;800&display=swap">
<style>
  :root {
    --burnt-orange: #e8891c;
    --burnt-orange-deep: #d9771a;
    --card-white: #f7f7f7;
    --ink: #1f1f1f;
    --backdrop: #2b2b2b;
  }
  * { margin: 0; padding: 0; box-sizing: border-box; }
  html, body {
    width: 1200px;
    height: 997px;
    overflow: hidden;
    background: var(--backdrop);
    font-family: "Montserrat", sans-serif;
  }
  .stage { position: relative; width: 1200px; height: 997px; }

  .card {
    position: absolute;
    width: 525px;
    height: 300px;
    border-radius: 22px;
    background: var(--card-white);
    overflow: hidden;
  }
  .card--front { left: 70px; top: 170px; }
  .card--back  { left: 605px; top: 470px; }

  .wordmark {
    display: flex;
    align-items: center;
    gap: 12px;
    color: var(--burnt-orange);
    font-weight: 800;
    letter-spacing: 2px;
  }
  .wordmark__dot {
    border-radius: 50%;
    background: var(--burnt-orange);
  }

  .card--front .wordmark {
    position: absolute;
    left: 0; right: 0; top: 118px;
    justify-content: center;
    font-size: 52px;
  }
  .card--front .wordmark__dot { width: 44px; height: 44px; }

  .card--back .wordmark {
    position: absolute;
    left: 0; right: 0; top: 38px;
    justify-content: center;
    font-size: 40px;
  }
  .card--back .wordmark__dot { width: 34px; height: 34px; }

  .contact-band {
    position: absolute;
    left: 0; right: 0;
    top: 132px;
    height: 118px;
    background: linear-gradient(90deg, var(--burnt-orange-deep), var(--burnt-orange));
  }
  .band-disc {
    position: absolute;
    left: 202px; top: 125px;
    width: 120px; height: 120px;
    border-radius: 50%;
    background: var(--card-white);
  }

  .holder {
    position: absolute;
    left: 40px; top: 182px;
  }
  .holder__name {
    font-size: 15px;
    font-weight: 800;
    letter-spacing: 1.5px;
    color: var(--ink);
  }
  .holder__role {
    font-size: 13px;
    font-weight: 600;
    color: var(--card-white);
    margin-left: 38px;
    margin-top: 2px;
  }

  .contact-list {
    position: absolute;
    right: 20px; top: 108px;
    list-style: none;
    text-align: right;
    font-size: 12px;
    font-weight: 500;
    color: var(--ink);
    line-height: 19px;
  }
  .contact-list li { display: flex; justify-content: flex-end; align-items: center; gap: 8px; }
  .contact-list .contact-icon { width: 13px; height: 13px; flex: none; }
  .contact-list .no-icon { padding-right: 21px; }

  .web-address {
    position: absolute;
    left: 0; right: 0; bottom: 16px;
    text-align: center;
    font-size: 13px;
    font-weight: 600;
    letter-spacing: 4px;
    color: var(--burnt-orange-deep);
  }
</style>
</head>
<body>
<main class="stage">
  <section class="card card--front" aria-label="Card front">
    <div class="wordmark"><span class="wordmark__dot"></span>VELQARA</div>
  </section>

  <section class="card card--back" aria-label="Card back">
    <div class="wordmark"><span class="wordmark__dot"></span>VELQARA</div>
    <div class="contact-band"></div>
    <div class="band-disc"></div>

    <div class="holder">
      <p class="holder__name">AMARA DELL</p>
      <p class="holder__role">Owner</p>
    </div>

    <ul class="contact-list">
      <li>0800 12 3400
        <svg class="contact-icon" viewBox="0 0 14 14"><circle cx="7" cy="7" r="7" fill="#f7f7f7"/><path d="M4.5 3.5l1.5 0 .6 2-1 .8a5 5 0 0 0 2.1 2.1l.8-1 2 .6 0 1.5c-3.5.4-6.4-2.5-6-6z" fill="#d9771a"/></svg>
      </li>
      <li>09 555 0142
        <svg class="contact-icon" viewBox="0 0 14 14"><circle cx="7" cy="7" r="7" fill="#f7f7f7"/><path d="M4.5 3.5l1.5 0 .6 2-1 .8a5 5 0 0 0 2.1 2.1l.8-1 2 .6 0 1.5c-3.5.4-6.4-2.5-6-6z" fill="#d9771a"/></svg>
      </li>
      <li>48 Harbour Lane Westfield
        <svg class="contact-icon" viewBox="0 0 14 14"><circle cx="7" cy="7" r="7" fill="#f7f7f7"/><path d="M7 3a2.6 2.6 0 0 0-2.6 2.6C4.4 7.6 7 11 7 11s2.6-3.4 2.6-5.4A2.6 2.6 0 0 0 7 3zm0 3.6a1 1 0 1 1 0-2 1 1 0 0 1 0 2z" fill="#d9771a"/></svg>
      </li>
      <li class="no-icon">North Auckland 0612</li>
    </ul>

    <p class="web-address">www.velqara.com</p>
  </section>
</main>
</body>
</html>
```